Photographic Tutorial website

We are looking for a fresh design for a photographic tutorial / workshop website. The website will have the included functions:

* Home (needs to have a login section)
* About Us
* Info about each course / workshop.
* Subscribe to courses and pay online.
* Members Area
* Photo gallery
* Contact us

The website will be implemented with our own made cms. We do not need it to be coded. We have a team ready to do this for us. We only need the PSD layout.

We have attached a mockup design that the client and I have come up with and we need the design to be taken to the next level.

Client also likes:
http://www.lumavistacamera.example/

Requirements
Must have
• Must Stand out i.e black backgrounds
Should not have
• Alter the logo in anyway.

```html
<!DOCTYPE html>
<html lang="en">
<head>
<meta charset="utf-8">
<title>Bright Frame Studio – Photographic Tuition</title>
<link href="https://fonts.googleapis.com/css2?family=Arimo:wght@400;700&family=Pathway+Gothic+One&family=Roboto+Condensed:wght@700&display=swap" rel="stylesheet">
<style>
:root{
  --bg-dark:#1b1b1b;
  --header:#1e1e1e;
  --side-gray:#7d7d7d;
  --footer:#7a7a7a;
  --green-dark:#14822c;
  --green-mid:#1bb33d;
  --green-light:#22f24f;
  --menu-green:#1f9a38;
  --white:#ffffff;
  --text-dark:#1a1a1a;
  --blue:#2a8fe0;
  --btn-blue:#52c5f2;
}
*{margin:0;padding:0;box-sizing:border-box}
html,body{width:1200px;height:1200px;overflow:hidden}
body{position:relative;background:var(--bg-dark);font-family:'Arimo',Arial,sans-serif;color:var(--white)}
.abs{position:absolute}
.site-header{left:0;top:0;width:1200px;height:63px;background:var(--header)}
.brand{left:88px;top:14px;display:flex;align-items:center;gap:10px}
.brand-mark{width:30px;height:30px;border-radius:50%;background:#d22}
.brand-name{font-family:'Roboto Condensed',sans-serif;font-weight:700;font-size:30px;color:var(--white);line-height:1}
.util-nav{right:92px;top:14px;font-size:11px}
.util-nav span{margin:0 6px}
.main-nav{top:38px;font-size:14px;font-weight:700}
.nav-active{left:561px;top:29px;width:101px;height:36px;background:var(--menu-green);border-radius:6px 6px 0 0;font-size:14px;font-weight:700;padding:9px 0 0 12px}
.hero{left:0;top:63px;width:1200px;height:396px;background:var(--side-gray)}
.hero-photo{left:87px;top:63px;width:1024px;height:396px;background:linear-gradient(180deg,#9a9c8c 0%,#6f7a55 40%,#3f5a22 75%,#5a7c2a 100%)}
.dropdown{left:561px;top:63px;width:202px;height:245px;background:linear-gradient(180deg,var(--green-dark),#2bb54a);padding:16px 10px 0 14px;font-size:12px;line-height:14px}
.dropdown li{list-style:none;padding:11px 40px 11px 0;border-bottom:1px solid rgba(255,255,255,.35);margin-right:0}
.dropdown li.wide{padding-right:0}
.dropdown li:last-child{border:none}
.section-title{font-family:'Pathway Gothic One',sans-serif;font-weight:400;font-size:30px;line-height:1;color:var(--white);white-space:nowrap}
.gallery{left:86px;top:522px;width:1024px;height:209px;border-radius:8px;background:linear-gradient(180deg,#fff,#d0d0d0)}
.thumb{top:542px;width:226px;height:170px;border-radius:8px}
.card{top:758px;width:304px;height:342px;border-radius:8px;overflow:hidden;background:linear-gradient(180deg,var(--green-dark) 0%,var(--green-mid) 50%,var(--green-light) 100%)}
.card-head{height:64px;background:linear-gradient(180deg,#fff,#e6e6e6);color:var(--text-dark);font-family:'Pathway Gothic One',sans-serif;font-size:26px;line-height:1;white-space:nowrap;padding:21px 0 0 26px;position:relative}
.card-head svg{position:absolute;right:16px;top:16px}
.checklist{list-style:none;padding:24px 0 0 22px;font-size:14px;font-weight:700}
.checklist li{height:30px;display:flex;align-items:flex-start;gap:11px}
.checklist li::before{content:"";width:11px;height:11px;margin-top:3px;border-radius:50%;background:var(--text-dark);box-shadow:inset 0 0 0 3px #0d3}
.btn-more{width:56px;height:25px;border-radius:5px;background:linear-gradient(180deg,#a8e6ff,var(--btn-blue));border:1px solid #1a5c7a;color:var(--text-dark);font-weight:700;font-size:14px;text-align:center;line-height:23px}
.post{position:absolute;left:33px}
.post-photo{position:absolute;left:0;top:0;width:100px;height:91px;border:1px solid #fff;background:linear-gradient(180deg,#4a5a78,#8a7a66)}
.post-text{position:absolute;left:115px;top:8px;width:141px;font-size:12px;line-height:18px;text-align:justify}
.post-text b{display:block;font-size:12px;margin-bottom:3px}
.quote{left:36px;top:90px;width:248px;height:140px;background:#fff;border-radius:4px;color:var(--text-dark);font-size:12px;line-height:18px;padding:15px 16px;text-align:justify}
.site-footer{left:0;top:1130px;width:1200px;height:70px;background:var(--footer);font-size:11px}
.site-footer span{margin:0 5px}
.social-badge{left:963px;top:1135px;width:146px;height:62px;border-radius:5px;background:linear-gradient(180deg,#5b7bc0,#2d4c93);border:2px solid #c8d3ea}
</style>
</head>
<body>
<header class="abs site-header">
  <div class="abs brand"><span class="brand-mark"></span><span class="brand-name">Bright Frame Studio</span></div>
  <nav class="abs util-nav">Home<span>|</span>About Us<span>|</span>Contact Us</nav>
  <div class="abs nav-active">Course info</div>
  <span class="abs main-nav" style="left:693px">Subscribe to courses</span>
  <span class="abs main-nav" style="left:882px">Members Area</span>
  <span class="abs main-nav" style="left:1021px">Photo gallery</span>
</header>

<section class="abs hero"></section>
<div class="abs hero-photo" role="img" aria-label="Misty forest with tall trees and green undergrowth"></div>
<svg class="abs" style="left:12px;top:206px" width="52" height="100"><polyline points="50,2 2,50 50,98" fill="none" stroke="#fff" stroke-width="1.5"/></svg>
<svg class="abs" style="left:1136px;top:206px" width="52" height="100"><polyline points="2,2 50,50 2,98" fill="none" stroke="#fff" stroke-width="1.5"/></svg>
<ul class="abs dropdown">
  <li>Night Photography</li>
  <li>Learning the basics of exposure, aventure, ISO &amp; compersition</li>
  <li class="wide">Learning your camera functions</li>
  <li>How to pick that good spot?</li>
  <li>What equipment do i need?</li>
</ul>

<h2 class="abs section-title" style="left:87px;top:479px">VIEW PHOTO GALLERY</h2>
<svg class="abs" style="left:1048px;top:478px" width="56" height="36">
  <polygon points="24,2 2,18 24,34" fill="var(--blue)"/><polygon points="32,2 54,18 32,34" fill="var(--blue)"/>
</svg>
<div class="abs gallery"></div>
<div class="abs thumb" style="left:111px;background:linear-gradient(180deg,#4a8fd8 0%,#9cc4e6 55%,#3d4a2a 75%,#2c3420 100%)" role="img" aria-label="Blue sky over distant mountains and trees"></div>
<div class="abs thumb" style="left:361px;background:linear-gradient(180deg,#2d6bb8 0%,#b78a5a 45%,#6a9ac8 70%,#2c6fb0 100%)" role="img" aria-label="Rock formation reflected in still water"></div>
<div class="abs thumb" style="left:611px;background:linear-gradient(180deg,#0d0d0d 0%,#5a3a10 45%,#c98a20 60%,#1a1410 100%)" role="img" aria-label="City skyline lit at night by a river"></div>
<div class="abs thumb" style="left:861px;background:linear-gradient(180deg,#2a2a30 0%,#6a5a40 35%,#1a3a3a 60%,#3a2a18 100%)" role="img" aria-label="Illuminated bridge and city lights at night"></div>

<section class="abs card" style="left:86px">
  <div class="card-head">PHOTOGRAPHER’S CHECK LIST<svg width="24" height="32"><polygon points="0,0 24,16 0,32" fill="#2fbf3f"/></svg></div>
  <ul class="checklist">
    <li>Lorem Lipsum Dolor Sit Amet</li><li>Lorem Lipsum Dolor Sit Amet</li><li>Lorem Lipsum Dolor Sit Amet</li>
    <li>Lorem Lipsum Dolor Sit Amet</li><li>Lorem Lipsum Dolor Sit Amet</li><li>Lorem Lipsum Dolor Sit Amet</li>
    <li>Lorem Lipsum Dolor Sit Amet</li>
  </ul>
  <div class="abs btn-more" style="left:221px;top:297px">more</div>
</section>

<section class="abs card" style="left:447px">
  <div class="card-head" style="padding-left:32px">PHOTOGRAPHY BLOG<svg width="24" height="32"><polygon points="0,0 24,16 0,32" fill="#2fbf3f"/></svg></div>
  <article class="post" style="top:88px">
    <div class="post-photo" role="img" aria-label="Bridge under a dramatic cloudy sky"></div>
    <p class="post-text"><b>POSTED ON 18-07-2012</b>Lorem Ipsum is simply dummy text of the printing and typesetting industry.</p>
  </article>
  <article class="post" style="top:208px">
    <div class="post-photo" role="img" aria-label="Bridge under a dramatic cloudy sky"></div>
    <p class="post-text"><b>POSTED ON 18-07-2012</b>Lorem Ipsum is simply dummy text of the printing and typesetting industry.</p>
  </article>
  <div class="abs btn-more" style="left:222px;top:297px">more</div>
</section>

<section class="abs card" style="left:806px">
  <div class="card-head" style="padding-left:32px">TESTIMONIALS<svg width="24" height="32"><polygon points="0,0 24,16 0,32" fill="#2fbf3f"/></svg></div>
  <blockquote class="abs quote">“Lorem Ipsum is simply dummy text of the printing and typesetting industry. Lorem Ipsum has been the industry's standard dummy text ever since the 1500s, when an unknown printer took a galley of type and scrambled”</blockquote>
  <svg class="abs" style="left:94px;top:229px" width="20" height="16"><polygon points="0,0 18,0 0,16" fill="#fff"/></svg>
  <p class="abs" style="left:57px;top:255px;font-size:14px;font-weight:700">- Lorem Lipsum</p>
  <div class="abs btn-more" style="left:229px;top:297px">more</div>
</section>

<footer class="abs site-footer">
  <p class="abs" style="left:86px;top:17px">Home<span>|</span>About Us<span>|</span>Course info<span>|</span>Subscribe to courses<span>|</span>Members Area<span>|</span>Photo gallery<span>|</span>Contact Us</p>
  <p class="abs" style="left:86px;top:38px">Copyrights ©&nbsp; 2012. All Rights Reserved.</p>
</footer>
<div class="abs social-badge" role="img" aria-label="Social network badge"></div>
</body>
</html>
```